1/2 Page add for BRMTL Conference

We are looking for a 1/2 page ad to support the annual BRMTL conference. I want to encourage the attendees to come to our both so we can explain how they can save money on food and supplies. here is a link to the conference. https://www.brmtl-example.org/conference/ here is our website www.pantrywisehub-example.com - the what we do can be captured in the ad. We will be at booth 505. Our goal is to get people to our booth #505 to explain the services that we provide –

Discounted food pricing
Free menu planning/design
Use of Registered Dietitian
Huge selection of discounted PPE and other necessary supplies to run any child care center

We have over 6000 members in 46 States and work with both small and large food distributors. We have been a sponsor of the association for the last 10 years.

Target Market(s)

Child care centers

Requirements
Must have
• Booth number -outline of what we do --- Stress we are a FREE service getting our members reduced pricing on food and supplies

```html
<!DOCTYPE html>
<html lang="en">
<head>
<meta charset="utf-8">
<title>PantryWise Hub – Conference Half-Page Ad</title>
<link href="https://fonts.googleapis.com/css2?family=Poppins:wght@400;500;600;700&display=swap" rel="stylesheet">
<style>
  :root {
    --page-bg: #3c3c3c;
    --white: #ffffff;
    --brand-blue: #2d8ae6;
    --navy: #0c1a3a;
    --logo-grey: #6d6f73;
    --ink: #333333;
  }
  * { margin: 0; padding: 0; box-sizing: border-box; }
  html, body { width: 1200px; height: 1200px; overflow: hidden; }
  body {
    background: var(--page-bg);
    font-family: "Poppins", sans-serif;
    position: relative;
  }
  .ad {
    position: absolute;
    left: 0; top: 192px;
    width: 1200px; height: 815px;
    overflow: hidden;
    background: var(--white);
  }
  .ad__photo {
    position: absolute; inset: 0 0 134px 0;
    background:
      linear-gradient(180deg, rgba(20,25,70,.55) 0%, rgba(20,20,50,.35) 55%, rgba(30,20,20,.45) 100%),
      radial-gradient(ellipse at 80% 75%, #d9932e 0%, rgba(190,110,40,0) 45%),
      radial-gradient(ellipse at 10% 60%, #7a6a2c 0%, rgba(90,80,40,0) 40%),
      linear-gradient(90deg, #5b4e3a 0%, #4b3f6a 35%, #3a3f70 60%, #5d4a52 100%);
  }
  .headline {
    position: absolute; left: 61px; top: 50px;
    color: var(--white);
    font-weight: 700;
    font-size: 84px;
    line-height: 69px;
    letter-spacing: -2px;
  }
  .headline span { display: block; }
  .rule {
    position: absolute; left: 61px; top: 413px;
    width: 625px; height: 2px; background: var(--white);
  }
  .event-meta {
    position: absolute; left: 61px; top: 428px;
    color: var(--white); font-size: 32px; font-weight: 400; letter-spacing: -0.5px;
  }
  .booth {
    position: absolute; left: 61px; top: 474px;
    color: var(--brand-blue); font-size: 32px; font-weight: 600; letter-spacing: -0.5px;
  }
  .services {
    position: absolute; left: 61px; top: 597px;
    color: var(--white); font-size: 23px; line-height: 34px; letter-spacing: -0.3px;
    list-style: none;
  }
  .services li { display: inline; }
  .services li::before {
    content: ""; display: inline-block; width: 9px; height: 9px;
    background: var(--brand-blue); margin: 0 6px 3px 0; vertical-align: middle;
  }
  .services li + li { margin-left: 4px; }
  .services .break { display: block; }
  .band { position: absolute; left: 0; bottom: 0; width: 1200px; height: 134px; }
  .brand {
    position: absolute; left: 88px; top: 712px;
    display: flex; align-items: center; gap: 14px;
  }
  .brand__mark { width: 26px; height: 26px; background: var(--brand-blue); }
  .brand__name { font-size: 34px; font-weight: 400; color: var(--logo-grey); letter-spacing: -1px; }
  .brand__tagline {
    position: absolute; left: 175px; top: 749px;
    font-size: 12px; color: var(--brand-blue); font-weight: 500;
  }
  .contact {
    position: absolute; left: 66px; top: 778px;
    font-size: 19px; color: var(--ink); display: flex; align-items: center; gap: 4px;
  }
  .contact svg { width: 16px; height: 16px; }
  .offer {
    position: absolute; left: 640px; width: 560px; top: 713px;
    text-align: center; color: var(--white);
    font-weight: 600; font-size: 25px; line-height: 32px; letter-spacing: -0.5px;
  }
  .offer em { font-style: normal; color: var(--navy); }
</style>
</head>
<body>
  <article class="ad">
    <div class="ad__photo" role="img" aria-label="Evening street scene in the New Orleans French Quarter with balconies, lit storefronts and city towers"></div>

    <h1 class="headline">
      <span>2022</span><span>National</span><span>Child</span><span>Nutrition</span><span>Conference</span>
    </h1>
    <div class="rule"></div>
    <p class="event-meta">April 18-22, 2022 | New Orleans, Louisiana</p>
    <p class="booth">BOOTH 505</p>

    <ul class="services">
      <li>Discounted Food Pricing</li>
      <li>Free Menu Planning/Design</li>
      <li>Use of Registered Dietitian</li>
      <li class="break">Huge selection of discounted PPE and other necessary supplies to run any child care center</li>
    </ul>

    <svg class="band" viewBox="0 0 1200 134" aria-hidden="true">
      <path d="M0,0 H480 C520,0 545,10 560,20 L1200,20 V134 H0 Z" fill="var(--white)"/>
      <path d="M553,20 H1200 V116 H700 C650,116 620,60 553,20 Z" fill="var(--brand-blue)"/>
    </svg>

    <div class="brand">
      <span class="brand__mark"></span>
      <span class="brand__name">PantryWise Hub</span>
    </div>
    <p class="brand__tagline">Your Hub for Savings</p>

    <p class="contact">
      <svg viewBox="0 0 24 24"><path d="M6.6 10.8a15 15 0 0 0 6.6 6.6l2.2-2.2a1 1 0 0 1 1-.25 11.4 11.4 0 0 0 3.6.6 1 1 0 0 1 1 1V20a1 1 0 0 1-1 1A17 17 0 0 1 3 4a1 1 0 0 1 1-1h3.5a1 1 0 0 1 1 1c0 1.25.2 2.45.6 3.6a1 1 0 0 1-.25 1z" fill="var(--brand-blue)"/></svg>
      555-010-4520 |
      <svg viewBox="0 0 24 24"><circle cx="12" cy="12" r="9" fill="none" stroke="var(--brand-blue)" stroke-width="2"/><path d="M3 12h18M12 3c3 3 3 15 0 18M12 3c-3 3-3 15 0 18" fill="none" stroke="var(--brand-blue)" stroke-width="1.6"/></svg>
      www.pantrywisehub-example.com
    </p>

    <p class="offer">MEMBERS GETS <em>FREE SERVICES ON</em><br>REDUCED PRICING ON FOOD &amp; SUPPLIES</p>
  </article>
</body>
</html>
```